Marlow Hire Business Card for recruitment company

We are looking for a Business Card Design that incorporates our personal details and our busines name and logo. We are a specialized search consultancy that recruit Property and Construction professionals.
We would like a business card that stands out and is appealing to the Construction and Property industry as well.

Target Market(s)

people in the construction and property industry

Contact Information for Business Card

Business Name and logo

Font styles to use
Serif

Colors
0094D4
00A9DD
6FCCEA
C7EBF8
E9F6FB

Requirements
Must have
• Business name and logo as well as contact details
Should not have
• No photos of us please

```html
<!DOCTYPE html>
<html lang="en">
<head>
<meta charset="utf-8">
<title>Marlow Hire – Business Card</title>
<link rel="stylesheet" href="https://fonts.googleapis.com/css2?family=Poppins:wght@300;400;500;600;700&display=swap">
<style>
  :root {
    --page-bg: #e3e3e5;
    --card-white: #ffffff;
    --ink-deep: #063f52;
    --ink-surname: #9ba4a8;
    --ink-muted: #6f7f86;
    --ink-label: #7d9aa5;
    --rule: #c9cfd2;
    --back-bg: #043a4d;
    --scene-light: #9bb3bc;
    --scene-dark: #3a6676;
    --back-scene: #2a5868;
  }
  * { box-sizing: border-box; margin: 0; padding: 0; }
  html, body {
    width: 705px; height: 1200px; overflow: hidden;
    background: var(--page-bg);
    font-family: "Poppins", sans-serif;
  }
  .sheet {
    width: 705px; height: 1200px;
    display: flex; flex-direction: column; align-items: center; justify-content: center;
    gap: 50px;
  }
  .card {
    position: relative;
    width: 600px; height: 341px;
    overflow: hidden;
    box-shadow: 8px 8px 10px rgba(0,0,0,0.22);
  }
  /* Front */
  .card-front { background: var(--card-white); }
  .front-scene { position: absolute; left: 0; top: 0; width: 600px; height: 341px; }
  .brand-name {
    position: absolute; left: 39px; top: 34px;
    font-weight: 300; font-size: 44px; letter-spacing: 1.5px;
    color: var(--ink-deep); line-height: 1; text-transform: uppercase;
  }
  .person-name {
    position: absolute; left: 39px; top: 131px;
    font-size: 27px; font-weight: 700; line-height: 28px; text-transform: uppercase;
    color: var(--ink-deep); letter-spacing: -0.3px;
  }
  .person-name .surname { font-weight: 400; color: var(--ink-surname); }
  .person-title {
    position: absolute; left: 40px; top: 159px;
    font-size: 11px; font-weight: 500; line-height: 14px; color: var(--ink-muted);
  }
  .person-rule { position: absolute; left: 40px; top: 179px; width: 42px; height: 1px; background: var(--rule); }
  .contact { position: absolute; left: 39px; top: 191px; list-style: none; }
  .contact li {
    display: flex; align-items: center; gap: 8px;
    font-size: 17px; font-weight: 600; color: var(--ink-deep); line-height: 22px;
  }
  .contact svg { width: 13px; height: 13px; flex: none; }
  .hours-label {
    position: absolute; left: 39px; top: 260px;
    display: flex; align-items: center; gap: 3px;
    font-size: 13px; font-weight: 500; line-height: 18px; color: var(--ink-label);
  }
  .hours-label svg { width: 12px; height: 12px; }
  .hours-days { position: absolute; left: 39px; top: 280px; font-size: 11px; line-height: 16px; color: var(--ink-deep); }
  .hours-time { position: absolute; left: 39px; top: 295px; font-size: 15px; line-height: 18px; color: var(--ink-deep); }
  .hours-time b { font-weight: 600; }
  /* Back */
  .card-back { background: var(--back-bg); }
  .back-scene { position: absolute; left: 0; top: 0; width: 600px; height: 341px; }
  .back-brand {
    position: absolute; left: 0; right: 0; top: 137px; text-align: center;
    font-weight: 300; font-size: 44px; letter-spacing: 1.5px; text-transform: uppercase;
    color: var(--card-white); line-height: 1;
  }
  .back-web {
    position: absolute; left: 0; right: 0; top: 283px; text-align: center;
    font-size: 14px; line-height: 18px; letter-spacing: 1.5px; color: var(--card-white);
  }
</style>
</head>
<body>
<main class="sheet">
  <section class="card card-front">
    <svg class="front-scene" viewBox="0 0 600 341" role="img" aria-label="Illustration area: construction workers, scaffolding and machinery in silhouette">
      <defs>
        <linearGradient id="sceneFade" x1="0" y1="0" x2="0" y2="1">
          <stop offset="0" stop-color="var(--scene-light)" stop-opacity="0"/>
          <stop offset="0.5" stop-color="var(--scene-light)" stop-opacity="0.7"/>
          <stop offset="1" stop-color="var(--scene-dark)"/>
        </linearGradient>
      </defs>
      <rect x="310" y="100" width="290" height="241" fill="url(#sceneFade)"/>
    </svg>
    <div class="brand-name">Marlow Hire</div>
    <div class="person-name">Nadia <span class="surname">Varga</span></div>
    <div class="person-title">Senior Search Consultant</div>
    <div class="person-rule"></div>
    <ul class="contact">
      <li>
        <svg viewBox="0 0 16 16" fill="none" stroke="var(--ink-muted)" stroke-width="1.3"><path d="M3 2l3 0 1 3-2 1.5c1 2 2.5 3.5 4.5 4.5L11 9l3 1v3c0 1-1 1.5-2 1.5C6 14 2 10 1.5 4 1.5 3 2 2 3 2z"/></svg>
        +64 21 555 0147
      </li>
      <li>
        <svg viewBox="0 0 16 16" fill="none" stroke="var(--ink-muted)" stroke-width="1.3"><rect x="1.5" y="3.5" width="13" height="9"/><path d="M1.5 3.5l6.5 5 6.5-5M1.5 12.5l5-4.5M14.5 12.5l-5-4.5"/></svg>
        n.varga@marlowhire.nz
      </li>
    </ul>
    <div class="hours-label">
      <svg viewBox="0 0 16 16" fill="none" stroke="var(--ink-label)" stroke-width="1.4"><circle cx="8" cy="8" r="6.3"/><path d="M8 4.5V8l2.5 1.5"/></svg>
      Business Hours
    </div>
    <div class="hours-days">Monday - Friday:</div>
    <div class="hours-time"><b>8:00</b>am - <b>6:00</b>pm NZST</div>
  </section>

  <section class="card card-back">
    <svg class="back-scene" viewBox="0 0 600 341" role="img" aria-label="Faint illustration area: construction silhouettes at both lower corners">
      <defs>
        <linearGradient id="backFade" x1="0" y1="0" x2="0" y2="1">
          <stop offset="0" stop-color="var(--back-scene)" stop-opacity="0"/>
          <stop offset="1" stop-color="var(--back-scene)"/>
        </linearGradient>
      </defs>
      <rect x="0" y="90" width="150" height="251" fill="url(#backFade)"/>
      <rect x="480" y="130" width="120" height="211" fill="url(#backFade)"/>
    </svg>
    <div class="back-brand">Marlow Hire</div>
    <div class="back-web">www.marlowhire.nz</div>
  </section>
</main>
</body>
</html>
```